Geek Gala Milwaukee monthly event poster template. Help make nerds cool!

We need a template for Geek Gala Milwaukee, a monthly event event that features three speakers on various topics. Geek Gala happens in cities worldwide but we need a pretty poster to list several details each month:
1. Geek Gala Milwaukee
2. Location
3. Time + date
4. Include the Geek Gala glasses (file options attached)
5. Something with the Milwaukee skyline or the outline of the shoreline with Lake Michigan or "Nerd iconography" (see below)
6. The colors white, orange, and blue.

Sorry for the short duration on this. I'm overwhelmed this week. Email with any questions. See GeekGala.com for other info. First event details will be Bramblewick Coffee Harbor Row, 7:30pm July 22nd

Target Market(s)

Coffee shop patrons, academics, hipsters, aged 21-40.

Industry/Entity Type

Event

Font styles to use
Serif

Colors
0493ce
f37122
ffffff

Requirements
Must have
• Geek Gala glasses
• "Geek Gala Milwaukee"
• Customizable slots for Location, Time, Date
Nice to have
• Something uniquely Milwaukee and/or a variety of "nerd" iconography (Telescope, microscope, plants, film, camera, monsters, pen, paintbrush, books)

```html
<!DOCTYPE html>
<html lang="en">
<head>
<meta charset="utf-8">
<title>Geek Gala Milwaukee — Event Poster</title>
<link rel="stylesheet" href="https://fonts.googleapis.com/css2?family=Russo+One&family=Arimo:wght@400&display=swap">
<style>
  :root {
    --backdrop: #eceded;
    --paper: #ffffff;
    --ink: #111111;
    --orange: #f37122;
    --orange-soft: #f4a06a;
    --blue: #0493ce;
    --blue-light: #53b1de;
    --blue-deep: #1d86c2;
    --rule: rgba(255,255,255,0.85);
  }
  html, body {
    margin: 0;
    padding: 0;
    width: 780px;
    height: 1200px;
    overflow: hidden;
    background: var(--backdrop);
  }
  .poster {
    position: absolute;
    left: 40px;
    top: 145px;
    width: 700px;
    height: 910px;
    background: var(--paper);
    overflow: hidden;
  }
  .title-block {
    position: absolute;
    left: 62px;
    top: 66px;
    height: 452px;
    display: flex;
    gap: 34px;
    align-items: flex-end;
  }
  .title-line {
    writing-mode: vertical-rl;
    transform: rotate(180deg);
    font-family: "Russo One", sans-serif;
    font-size: 80px;
    line-height: 1;
    margin: 0;
    white-space: nowrap;
  }
  .title-event { color: var(--ink); }
  .title-city { color: var(--orange); }

  .glasses-art {
    position: absolute;
    left: 64px;
    top: 590px;
    width: 450px;
    height: 180px;
    border-radius: 90px 30px 90px 30px;
    background: linear-gradient(150deg, var(--orange-soft), var(--orange));
    opacity: 0.9;
    z-index: 2;
  }

  .brand-mark {
    position: absolute;
    left: 30px;
    top: 820px;
    display: flex;
    align-items: center;
    gap: 8px;
    font-family: "Arimo", sans-serif;
    font-size: 18px;
    line-height: 1;
    color: var(--blue);
    z-index: 3;
  }
  .brand-mark .dot {
    width: 18px;
    height: 18px;
    border-radius: 50%;
    background: var(--blue);
  }

  .details-panel {
    position: absolute;
    left: 325px;
    top: 0;
    width: 375px;
    height: 910px;
    background: linear-gradient(180deg, var(--blue-light), var(--blue) 55%, var(--blue-deep));
  }
  .detail {
    position: absolute;
    left: 0;
    width: 296px;
    text-align: center;
    font-family: "Arimo", sans-serif;
    font-size: 28px;
    line-height: 36px;
    color: var(--paper);
    margin: 0;
  }
  .detail-location { top: 122px; }
  .detail-date { top: 285px; }
  .detail-time { top: 415px; color: var(--orange); }
  .divider {
    position: absolute;
    left: 0;
    width: 274px;
    height: 2px;
    background: var(--rule);
  }
  .divider-one { top: 236px; }
  .divider-two { top: 365px; }

  .skyline-art {
    position: absolute;
    right: 0;
    top: 0;
    width: 72px;
    height: 910px;
    background: linear-gradient(180deg, var(--orange-soft), var(--orange));
  }
</style>
</head>
<body>
  <main class="poster">
    <div class="title-block">
      <h1 class="title-line title-event">Geek Gala</h1>
      <p class="title-line title-city">Milwaukee</p>
    </div>

    <div class="glasses-art" role="img" aria-label="Orange Geek Gala glasses illustration"></div>

    <div class="brand-mark">
      <span class="dot"></span>
      <span>Geek Gala</span>
    </div>

    <section class="details-panel">
      <p class="detail detail-location">Bramblewick Coffee<br>Harbor Row</p>
      <div class="divider divider-one"></div>
      <p class="detail detail-date">July 22nd</p>
      <div class="divider divider-two"></div>
      <p class="detail detail-time">7:30pm</p>
      <div class="skyline-art" role="img" aria-label="Orange Milwaukee skyline silhouette"></div>
    </section>
  </main>
</body>
</html>
```